PYLON SIGN FOR “MEADOWLARK CAR WASH RAPID”

please see the new images in my brief. I have a logo design and the colors I would like you to follow.

please put "meadowlark car wash rapid" in the logo

Target Market(s)

GENERAL PUBLIC

Industry/Entity Type

CAR WASH

Font styles to use
Other font styles liked:
• CURSIVE AND BLOCK LETTERING BOTH AS IN THE SAMPLE PIC

Colors
00AB8E
00BBA5
67D7C9
C6EFE9
E9F9F6
6B429C
8869AF
B7A5CE
E3DAEB
F3F0F8

Requirements
Must have
• 1. “MEADOWLARK CAR WASH RAPID” PLEASE PUT THIS IN THE LOGO 2. USE BLACK, WHITE, GREEN AND SILVER FOR A COLOR
Nice to have
• I WOULD LIKE TO SEE THE SIGN IN BOTH COLOR THEMES: WHITE, BLACK, GREEN AND SILVER AND WHITE BLACK PURPLE AND SILVER

```html
<!DOCTYPE html>
<html lang="en">
<head>
<meta charset="utf-8">
<title>Meadowlark Car Wash Rapid – Pylon Sign</title>
<link rel="stylesheet" href="https://fonts.googleapis.com/css2?family=Montserrat:wght@800&display=swap">
<style>
  :root {
    --backdrop-light: #f2f2f2;
    --backdrop-dark: #1c1c1c;
    --sign-green: #009146;
    --divider-white: #ffffff;
    --band-dark: #1e1e1e;
    --band-mid: #5a5a5a;
    --text-white: #ffffff;
    --brand-silver: #dcdfe2;
    --icon-green: #0a9a48;
  }
  * { margin: 0; padding: 0; box-sizing: border-box; }
  html, body {
    width: 818px;
    height: 1200px;
    overflow: hidden;
  }
  body {
    background: linear-gradient(135deg, var(--backdrop-dark) 0%, #9a9a9a 45%, var(--backdrop-light) 60%, #b5b5b5 80%, var(--backdrop-dark) 100%);
    position: relative;
    font-family: "Montserrat", sans-serif;
  }
  .pylon-sign {
    position: absolute;
    left: 29px;
    top: 310px;
    width: 760px;
    height: 581px;
    box-shadow: 0 10px 30px rgba(0, 0, 0, 0.45);
    display: flex;
    flex-direction: column;
  }
  .brand-panel {
    flex: 0 0 433px;
    background: var(--sign-green);
    display: flex;
    flex-direction: column;
    align-items: center;
    justify-content: center;
    color: var(--brand-silver);
    font-weight: 800;
    text-align: center;
    line-height: 1;
  }
  .brand-mark {
    width: 96px;
    height: 96px;
    border-radius: 50%;
    background: var(--brand-silver);
    margin-bottom: 30px;
  }
  .brand-name__primary {
    font-size: 70px;
    letter-spacing: 0;
  }
  .brand-name__secondary {
    font-size: 40px;
    letter-spacing: 3px;
    margin-top: 18px;
  }
  .panel-divider {
    flex: 0 0 5px;
    background: var(--divider-white);
  }
  .contact-band {
    flex: 1;
    background: linear-gradient(90deg, var(--band-mid) 0%, #3a3a3a 45%, var(--band-dark) 100%);
    display: flex;
    align-items: center;
    justify-content: center;
    gap: 22px;
  }
  .phone-icon {
    width: 68px;
    height: 68px;
    flex: 0 0 68px;
  }
  .phone-number {
    color: var(--text-white);
    font-weight: 800;
    font-size: 66px;
    letter-spacing: -1px;
  }
</style>
</head>
<body>
  <main class="pylon-sign">
    <section class="brand-panel" aria-label="Meadowlark Car Wash Rapid">
      <div class="brand-mark" aria-hidden="true"></div>
      <span class="brand-name__primary">MEADOWLARK</span>
      <span class="brand-name__secondary">CAR WASH RAPID</span>
    </section>
    <div class="panel-divider"></div>
    <section class="contact-band">
      <svg class="phone-icon" viewBox="0 0 70 70" aria-hidden="true">
        <circle cx="35" cy="35" r="35" fill="#ffffff"/>
        <path d="M25 20 l6 -2 l5 10 l-4 4 c2 5 5 8 10 10 l4 -4 l10 5 l-2 6 c-18 2 -31 -11 -29 -29 z"
              fill="none" stroke="var(--icon-green)" stroke-width="2.5" stroke-linejoin="round"/>
        <path d="M39 22 a10 10 0 0 1 9 9 M40 15 a17 17 0 0 1 15 15"
              fill="none" stroke="var(--icon-green)" stroke-width="2.5" stroke-linecap="round"/>
      </svg>
      <span class="phone-number">(555) 014-2739</span>
    </section>
  </main>
</body>
</html>
```